Business Card

Just need business logo with phone number on it. 0487 312 556
And the following on the bottom of the card.

"Your local plumbing experts".
and emblems for kelpa card, cheque and cash

```html
<!DOCTYPE html>
<html lang="en">
<head>
<meta charset="utf-8">
<title>Ridgeline Plumbing &amp; Drainage – Business Card</title>
<link rel="stylesheet" href="https://fonts.googleapis.com/css2?family=Open+Sans:wght@400;600;700&display=swap">
<style>
  :root {
    --backdrop: #e9e6e2;
    --card: #050505;
    --brand-grey: #9a9a9a;
    --brand-red: #e8202a;
    --brand-blue: #2a92d6;
    --text-white: #ffffff;
    --shadow: rgba(0, 0, 0, 0.35);
  }
  html, body {
    margin: 0;
    padding: 0;
    width: 1200px;
    height: 1000px;
    overflow: hidden;
    background: var(--backdrop);
    font-family: "Open Sans", Arial, sans-serif;
  }
  .canvas {
    position: relative;
    width: 1200px;
    height: 1000px;
  }
  .card {
    position: absolute;
    left: 266px;
    width: 666px;
    height: 397px;
    background: var(--card);
    box-shadow: 0 6px 16px var(--shadow);
    color: var(--text-white);
    text-align: center;
  }
  .card--front { top: 74px; }
  .card--back { top: 533px; }

  .brand {
    position: absolute;
    left: 0;
    right: 0;
    display: flex;
    align-items: center;
    justify-content: center;
    gap: 14px;
  }
  .card--front .brand { top: 205px; }
  .card--back .brand { top: 68px; }

  .brand__mark {
    width: 18px;
    height: 18px;
    border-radius: 50%;
    flex: none;
  }
  .brand__name {
    font-weight: 700;
    font-size: 30px;
    letter-spacing: 2px;
    line-height: 1.1;
    text-transform: uppercase;
  }
  .card--front .brand__name,
  .card--front .brand__mark { color: var(--brand-grey); background: none; }
  .card--front .brand__mark { background: var(--brand-grey); }
  .card--back .brand__name { color: var(--brand-red); }
  .card--back .brand__mark { background: var(--brand-red); }

  .contact {
    position: absolute;
    top: 210px;
    left: 0;
    right: 0;
  }
  .contact__name {
    margin: 0 0 8px;
    font-size: 20px;
    font-weight: 700;
    color: var(--brand-red);
    letter-spacing: 0.5px;
  }
  .contact__line {
    margin: 0;
    font-size: 16px;
    line-height: 22px;
  }
  .tagline {
    margin: 12px 0 0;
    font-size: 16px;
    font-weight: 600;
    line-height: 22px;
  }
  .payments {
    margin: 0;
    font-size: 16px;
    line-height: 24px;
  }
</style>
</head>
<body>
<main class="canvas">
  <section class="card card--front" aria-label="Card front">
    <div class="brand">
      <span class="brand__mark" aria-hidden="true"></span>
      <span class="brand__name">Ridgeline Plumbing<br>&amp; Drainage</span>
    </div>
  </section>

  <section class="card card--back" aria-label="Card back">
    <div class="brand">
      <span class="brand__mark" aria-hidden="true"></span>
      <span class="brand__name">Ridgeline Plumbing<br>&amp; Drainage</span>
    </div>
    <div class="contact">
      <p class="contact__name">DYLAN CARRICK</p>
      <p class="contact__line">0487 312 556</p>
      <p class="contact__line">info@ridgelineplumbing.com.au</p>
      <p class="tagline">“Your local plumbing experts"</p>
      <p class="payments">Emblems for kelpa card, cheque and cash</p>
    </div>
  </section>
</main>
</body>
</html>
```